Wanderlark Gin - Bottle Label for a craft Gin about to be launched on the world from New Zealand

We are a start up craft distillery in New Zealand. We have developed a wonderful Gin using our own grain spirit and both traditional and New Zealand native botanicals (Manuka to be specific), chosen our bottle and the name "Wanderlark" and done a bit of amateur label design and now we are looking for someone to make it great.

Feel free to change up our amateur concept but give us something that will pop from the back bar and scream authenticity, craft and individuality.

The attached files give you the specifications of the bottle, our current concept for a Wanderlark label and an earlier concept drawing that gives an idea of where we are thinking the two labels should go on the front of the bottle.

Thanks, we look forward to your ideas!!

Target Market(s)

High end and craft Gin drinkers. Hipsters and cocktail barflys and their bar tenders and bar owners

Requirements
Must have
• Attractive individuality
Nice to have
• Coolness
Should not have
• Uncoolness

```html
<!DOCTYPE html>
<html lang="en">
<head>
<meta charset="utf-8">
<title>Wanderlark Gin – Wild Drift Label</title>
<link href="https://fonts.googleapis.com/css2?family=Kaushan+Script&family=Tinos:wght@400;700&display=swap" rel="stylesheet">
<style>
  :root {
    --gold-dark: #c08a34;
    --gold-mid: #dca552;
    --gold-light: #f3d48c;
    --panel: #fdf8b4;
    --maroon: #8c1b22;
    --ink: #1c1c1c;
    --glass-edge: #c9ccd0;
    --glass-fill: #f4f6f8;
    --petal: #e7b5d8;
    --leaf: #5d7a3a;
    --white: #ffffff;
  }
  html, body {
    margin: 0;
    width: 1026px;
    height: 1200px;
    overflow: hidden;
    background: var(--white);
  }
  .artboard { display: block; width: 1026px; height: 1200px; }
  .script { font-family: "Kaushan Script", cursive; fill: var(--maroon); }
  .serif { font-family: "Tinos", serif; }
  .tagline { fill: var(--ink); }
  .volume { fill: var(--maroon); font-weight: 700; }
  .wordmark { fill: var(--white); font-weight: 400; }
  .recipe-title { fill: #4a2a14; }
  .recipe-line { stroke: var(--ink); stroke-width: 5; }
  .panel { fill: var(--panel); }
  .keyline { fill: none; stroke: var(--white); stroke-width: 2; opacity: .8; }
  .crest-band { fill: var(--maroon); stroke: var(--gold-light); stroke-width: 3; }
</style>
</head>
<body>
<svg class="artboard" viewBox="0 0 1026 1200" xmlns="http://www.w3.org/2000/svg">
  <defs>
    <linearGradient id="gold" x1="0" y1="0" x2="1" y2="1">
      <stop offset="0" stop-color="#f3d48c"/>
      <stop offset=".45" stop-color="#dca552"/>
      <stop offset="1" stop-color="#c08a34"/>
    </linearGradient>
    <linearGradient id="glass" x1="0" y1="0" x2="1" y2="0">
      <stop offset="0" stop-color="#dfe2e5"/>
      <stop offset=".3" stop-color="#f4f6f8"/>
      <stop offset=".7" stop-color="#ffffff"/>
      <stop offset="1" stop-color="#d8dbdf"/>
    </linearGradient>
    <radialGradient id="blossom" cx=".5" cy=".5" r=".6">
      <stop offset="0" stop-color="#e7b5d8"/>
      <stop offset=".75" stop-color="#c99bc0"/>
      <stop offset="1" stop-color="#5d7a3a" stop-opacity=".6"/>
    </radialGradient>
    <linearGradient id="wheat" x1="0" y1="0" x2="0" y2="1">
      <stop offset="0" stop-color="#f3d48c"/>
      <stop offset="1" stop-color="#c08a34"/>
    </linearGradient>
  </defs>

  <!-- Bottle -->
  <g class="bottle" role="img" aria-label="Clear glass gin bottle with gold foil cap">
    <path d="M182 220 L182 330 C182 380 96 400 96 450 L96 1120 Q96 1150 126 1150 L330 1150 Q360 1150 360 1120 L360 450 C360 400 254 380 254 330 L254 220 Z"
          fill="url(#glass)" stroke="var(--glass-edge)" stroke-width="3"/>
    <path d="M180 112 Q180 106 188 106 L248 106 Q256 106 256 112 L258 232 L178 232 Z" fill="url(#gold)"/>
  </g>

  <!-- Front label on bottle -->
  <g class="bottle-label">
    <rect x="107" y="488" width="227" height="214" rx="20" fill="url(#gold)"/>
    <rect x="113" y="494" width="215" height="202" rx="16" class="keyline"/>
    <rect x="128" y="515" width="186" height="145" rx="14" class="panel"/>
    <rect x="110" y="514" width="46" height="46" rx="20" fill="url(#blossom)" role="img" aria-label="Pink blossom sprig"/>
    <rect x="285" y="630" width="46" height="46" rx="20" fill="url(#blossom)" role="img" aria-label="Pink blossom sprig"/>
    <ellipse cx="220" cy="493" rx="38" ry="20" fill="url(#gold)" stroke="var(--maroon)" stroke-width="2"/>
    <rect x="184" y="485" width="72" height="16" rx="5" class="crest-band"/>
    <text x="220" y="496.5" text-anchor="middle" class="serif wordmark" font-size="9" textLength="58" lengthAdjust="spacingAndGlyphs">WANDERLARK</text>
    <text x="220" y="588" text-anchor="middle" class="script" font-size="38">Wild Drift</text>
    <text x="220" y="610" text-anchor="middle" class="serif tagline" font-size="14">SMALL BATCH GIN</text>
    <text x="220" y="680" text-anchor="middle" class="serif volume" font-size="15">500 ml</text>
  </g>

  <!-- Recipe label on bottle -->
  <g class="recipe-label">
    <path d="M134 925 L134 815 Q134 784 165 784 L290 784 Q321 784 321 815 L321 925 Z" fill="url(#gold)"/>
    <path d="M146 918 L146 820 Q146 796 170 796 L285 796 Q309 796 309 820 L309 918 Z" class="panel"/>
    <text x="228" y="828" text-anchor="middle" class="serif recipe-title" font-size="22">RECIPE #3</text>
    <line x1="172" y1="848" x2="286" y2="848" class="recipe-line"/>
    <line x1="172" y1="864" x2="286" y2="864" class="recipe-line"/>
    <line x1="172" y1="880" x2="286" y2="880" class="recipe-line"/>
    <line x1="190" y1="896" x2="266" y2="896" class="recipe-line"/>
  </g>

  <!-- Main label, flat -->
  <g class="main-label">
    <rect x="428" y="168" width="524" height="475" rx="44" fill="url(#gold)"/>
    <rect x="440" y="180" width="500" height="451" rx="36" class="keyline"/>
    <rect x="470" y="218" width="441" height="345" rx="34" class="panel"/>
    <rect x="432" y="205" width="130" height="125" rx="55" fill="url(#blossom)" role="img" aria-label="Cluster of pink manuka blossoms with leaves"/>
    <rect x="800" y="480" width="135" height="130" rx="55" fill="url(#blossom)" role="img" aria-label="Cluster of pink manuka blossoms with leaves"/>
    <ellipse cx="690" cy="184" rx="90" ry="48" fill="url(#gold)" stroke="var(--maroon)" stroke-width="3"/>
    <rect x="610" y="166" width="160" height="36" rx="10" class="crest-band"/>
    <text x="690" y="191" text-anchor="middle" class="serif wordmark" font-size="20" textLength="134" lengthAdjust="spacingAndGlyphs">WANDERLARK</text>
    <text x="690" y="410" text-anchor="middle" class="script" font-size="88">Wild Drift</text>
    <text x="690" y="462" text-anchor="middle" class="serif tagline" font-size="32">SMALL BATCH GIN</text>
    <text x="690" y="612" text-anchor="middle" class="serif volume" font-size="34">500 ml</text>
  </g>

  <!-- Round badge -->
  <g class="badge">
    <circle cx="690" cy="851" r="140" fill="url(#gold)"/>
    <circle cx="690" cy="851" r="118" fill="var(--white)"/>
    <rect x="630" y="745" width="120" height="55" rx="25" fill="url(#blossom)" role="img" aria-label="Row of pink blossoms"/>
    <rect x="565" y="818" width="250" height="68" rx="32" class="crest-band"/>
    <text x="690" y="863" text-anchor="middle" class="serif wordmark" font-size="30" textLength="196" lengthAdjust="spacingAndGlyphs">WANDERLARK</text>
    <rect x="640" y="902" width="100" height="40" rx="18" fill="url(#wheat)" role="img" aria-label="Wheat sprig ornament"/>
  </g>
</svg>
</body>
</html>
```